Healthy lifestyle Influencer business card

I need your creativity to have a business card that I can leave in all the restaurants, hotels and spas I visit to inform them that I am an influencer specializing in the wellness sector and that I will write a review about them. You can use my instagram photos Lunavivo27 or on my website www.piattileggerisani.it. I would like my business card to impress with its creativity! thank you very much!

Contact Information for Business Card

siteweb, instagram, phone number

Font styles to use
Decorative
Script

Colors
0094D4
00A9DD
6FCCEA
C7EBF8
E9F6FB
59FF00
82FF00
B8FF75
E3FFCB
F4FFEA
FFC000
F8CF3A
FAE287
FDF2CF
FEFAEE
F0912C
F2A743
F7CA91
FBE8D2
FDF5EE
EE7325
F08F49
F5BC92
FAE3D3
FDF4ED
EB3D1F
EC4F4E
F09395
F8D3D4
FCEDEE
E54698
E96AAD
F1A4CE
F9D9EA
FCEFF6

Requirements
Nice to have
• creativity

```html
<!DOCTYPE html>
<html lang="en">
<head>
<meta charset="utf-8">
<title>Lunavivo Chef – Business Card</title>
<link rel="stylesheet" href="https://fonts.googleapis.com/css2?family=Nunito+Sans:wght@400;600&display=swap">
<style>
  :root {
    --page-bg: #eeeae8;
    --card-dark: #545454;
    --accent-teal: #93c2b6;
    --text-light: #ffffff;
    --logo-ink: #3f3f3f;
    --frost-light: #fbf6f5;
    --frost-blush: #f1dcdc;
    --edge-blush: #e9cfd0;
  }
  html, body {
    margin: 0;
    width: 1200px;
    height: 900px;
    overflow: hidden;
    background: var(--page-bg);
  }
  .business-card {
    position: absolute;
    left: 100px;
    top: 140px;
    width: 1000px;
    height: 619px;
    box-shadow: 0 10px 30px rgba(0,0,0,0.15);
  }
  .business-card svg {
    display: block;
    width: 100%;
    height: 100%;
  }
  .card-text {
    font-family: "Nunito Sans", sans-serif;
  }
  .holder-name { fill: var(--accent-teal); font-size: 36px; font-weight: 600; letter-spacing: 0.5px; }
  .holder-role, .address-line, .contact-line { fill: var(--text-light); font-size: 30px; font-weight: 400; }
  .brand-name { fill: var(--logo-ink); font-size: 46px; font-weight: 400; }
  .contact-icon { fill: none; stroke: var(--accent-teal); stroke-width: 2.5; }
  .contact-icon-solid { fill: var(--accent-teal); }
</style>
</head>
<body>
  <div class="business-card">
    <svg viewBox="0 0 1090 675" xmlns="http://www.w3.org/2000/svg">
      <defs>
        <radialGradient id="frost-fill" cx="0.45" cy="0.5" r="0.7">
          <stop offset="0" stop-color="var(--frost-light)"/>
          <stop offset="0.6" stop-color="#f6ecec"/>
          <stop offset="1" stop-color="var(--frost-blush)"/>
        </radialGradient>
        <clipPath id="card-clip"><rect width="1090" height="675"/></clipPath>
      </defs>

      <g clip-path="url(#card-clip)">
        <rect class="card-base" width="1090" height="675" fill="var(--card-dark)"/>

        <path class="heart-panel" role="img" aria-label="Frosted translucent heart panel with soft blush tones"
              fill="url(#frost-fill)"
              d="M0,0 L112,0 C170,55 225,115 255,152 C330,60 420,0 480,0 C600,0 668,60 662,175 C652,335 500,525 275,675 L0,675 Z"/>

        <path class="heart-edge-blush" fill="none" stroke="var(--edge-blush)" stroke-width="4"
              d="M485,-2 C608,-2 675,62 668,178 C658,340 505,530 280,678"/>
        <path class="heart-outline" fill="none" stroke="var(--accent-teal)" stroke-width="5"
              d="M112,0 C170,55 225,115 255,152 C330,60 420,0 480,0 C600,0 662,60 655,172 C645,330 495,520 268,678"/>
      </g>

      <text class="card-text brand-name" x="275" y="345" text-anchor="middle">Lunavivo Chef</text>

      <g class="card-text" text-anchor="end">
        <text class="holder-name" x="1025" y="140">JONATHAN SMITH</text>
        <text class="holder-role" x="1025" y="174">Managing Director</text>

        <text class="address-line" x="1025" y="342">421, Address line</text>
        <text class="address-line" x="1025" y="382">goes here</text>
        <text class="address-line" x="1025" y="421">45452,Country Name</text>

        <text class="contact-line" x="986" y="515">044-123 456 789</text>
        <text class="contact-line" x="986" y="555">info@webname.com</text>
        <text class="contact-line" x="986" y="595">www.websitename.com</text>
      </g>

      <g class="contact-icons">
        <path class="contact-icon" d="M999,495 c-3,3 -3,9 2,15 c5,6 11,9 15,6 l2,-3 l-5,-5 l-3,2 c-2,-1 -5,-4 -6,-7 l2,-3 l-5,-5 z"/>
        <path class="contact-icon" d="M1010,496 a8,8 0 0 1 8,8 M1010,491 a13,13 0 0 1 13,13"/>
        <rect class="contact-icon-solid" x="998" y="536" width="26" height="18"/>
        <path d="M998,536 l13,10 l13,-10" fill="none" stroke="var(--card-dark)" stroke-width="2"/>
        <circle class="contact-icon" cx="1011" cy="585" r="12"/>
        <ellipse class="contact-icon" cx="1011" cy="585" rx="5" ry="12"/>
        <path class="contact-icon" d="M999,585 h24 M1001,579 h20 M1001,591 h20"/>
      </g>
    </svg>
  </div>
</body>
</html>
```